Construction company needs upscale elegant truck and trailer design

Hello,
I am looking for a wrap design for my Velmark ridgeback truck and my 6x12 cargo trailer. I want to advertise my remodeling business, but I want it to be elegant and upscale. We work on commercial and residential projects with a specialization in historic homes and interior buildouts.
Our website is www.brookpierbuilders.example.
We cater to upscale clientele and I don't want it to be too flashy. I don't want anything on the back glass. I also don't want a full vehicle wrap to keep the cost down. I want a partial wrap that goes towards the back, nothing on the hood. The phone number is 555-281-3390.

Target Market(s)

Historic Restoration - New Construction - Remodeling

Industry/Entity Type

Luxury Construction Remodeling

Colors

Designer to choose colors to be used in the design.

Requirements
Must have
• truck and trailer
Nice to have
• My truck is silver with black rims, so I want it to match nice with what I already have.

```html
<!DOCTYPE html>
<html lang="en">
<head>
<meta charset="utf-8">
<title>Brookpier Builders – Truck and Trailer Wrap</title>
<link rel="stylesheet" href="https://fonts.googleapis.com/css2?family=Tinos:wght@700&family=Cormorant+Garamond:wght@500&family=Poppins:wght@400;600&display=swap">
<style>
  :root {
    --canvas: #ffffff;
    --silver: #a8a59f;
    --silver-light: #bdbab4;
    --ink: #111111;
    --band: #0c0c0c;
    --white: #ffffff;
    --sketch-a: #b3b0aa;
    --sketch-b: #96938d;
  }
  html, body {
    margin: 0;
    padding: 0;
    width: 1200px;
    height: 1200px;
    overflow: hidden;
    background: var(--canvas);
  }
  .wrap-sheet {
    position: relative;
    width: 1200px;
    height: 1200px;
  }
  .panel { position: absolute; display: block; }
  .truck-panel { left: 60px; top: 130px; width: 1080px; height: 420px; }
  .trailer-panel { left: 290px; top: 650px; width: 620px; height: 400px; }
  .body-fill { fill: var(--silver); }
  .band-fill { fill: var(--band); }
  .rule { stroke: var(--ink); stroke-width: 1; }
  .title {
    font-family: "Tinos", "Times New Roman", serif;
    font-weight: 700;
    fill: var(--ink);
    letter-spacing: 1px;
  }
  .caption {
    font-family: "Cormorant Garamond", Georgia, serif;
    font-weight: 500;
    fill: var(--ink);
  }
  .phone {
    font-family: "Poppins", Arial, sans-serif;
    font-weight: 600;
    fill: var(--white);
    letter-spacing: 1px;
  }
  .tagline {
    font-family: "Poppins", Arial, sans-serif;
    font-weight: 400;
  }
  .tagline-dark { fill: var(--ink); }
  .tagline-light { fill: var(--white); }
</style>
</head>
<body>
<main class="wrap-sheet">

  <svg class="panel truck-panel" viewBox="0 0 1080 420" aria-label="Truck side wrap layout">
    <defs>
      <linearGradient id="sketchTone" x1="0" y1="0" x2="1" y2="1">
        <stop offset="0" stop-color="var(--sketch-a)"/>
        <stop offset="1" stop-color="var(--sketch-b)"/>
      </linearGradient>
    </defs>
    <rect class="body-fill" x="0" y="40" width="1080" height="340" rx="28"/>
    <polygon role="img" aria-label="Line sketch of a kitchen interior with bar stools" fill="url(#sketchTone)"
             points="700,178 1060,178 1060,360 590,360"/>
    <polygon class="band-fill" points="610,80 1068,80 1068,128 714,128 566,372 468,372"/>
    <rect class="band-fill" x="20" y="362" width="470" height="10"/>
    <text class="phone" x="740" y="116" font-size="34">555-281-3390</text>
    <text class="tagline tagline-dark" x="760" y="160" font-size="17">commercial and residential</text>
    <text class="title" x="270" y="195" font-size="52" text-anchor="middle">BROOKPIER</text>
    <text class="title" x="270" y="250" font-size="40" text-anchor="middle">BUILDERS</text>
    <line class="rule" x1="70" y1="290" x2="470" y2="290"/>
    <text class="caption" x="72" y="312" font-size="16" textLength="396" lengthAdjust="spacingAndGlyphs">BrookpierBuilders.example * Certified Building Contractor #047318</text>
    <line class="rule" x1="70" y1="322" x2="470" y2="322"/>
  </svg>

  <svg class="panel trailer-panel" viewBox="0 0 620 400" aria-label="Cargo trailer side wrap layout">
    <defs>
      <linearGradient id="trailerSketch" x1="0" y1="0" x2="1" y2="1">
        <stop offset="0" stop-color="var(--sketch-a)"/>
        <stop offset="1" stop-color="var(--sketch-b)"/>
      </linearGradient>
    </defs>
    <rect class="body-fill" x="0" y="0" width="620" height="400" rx="6"/>
    <rect role="img" aria-label="Line sketch of a kitchen with island, sink and bar stools" fill="url(#trailerSketch)"
          x="0" y="248" width="620" height="152"/>
    <text class="title" x="310" y="62" font-size="50" text-anchor="middle">BROOKPIER</text>
    <text class="title" x="310" y="112" font-size="38" text-anchor="middle">BUILDERS</text>
    <line class="rule" x1="75" y1="142" x2="545" y2="142"/>
    <text class="caption" x="80" y="166" font-size="18" textLength="460" lengthAdjust="spacingAndGlyphs">BrookpierBuilders.example * Certified Building Contractor #047318</text>
    <line class="rule" x1="75" y1="176" x2="545" y2="176"/>
    <rect class="band-fill" x="0" y="194" width="620" height="46"/>
    <text class="phone" x="60" y="229" font-size="30">555-281-3390</text>
    <rect fill="var(--white)" x="328" y="203" width="2" height="28"/>
    <text class="tagline tagline-light" x="355" y="225" font-size="16">commercial and residential</text>
  </svg>

</main>
</body>
</html>
```